AUSTRALIAN CONSULTING FIRM BUSINESS CARD - MODERN

We are wanting a modern, clean lined business card design. We are professional niche consultancy firm situated in Australia called Harbrook Advisory Partners Pty Ltd.
The card should communicate professionalism and creativity and draw on our logo design (attached).
The design should be two sided, landscape orientation.
Target Market(s)
government, not for profit sector, corporate clients
Industry/Entity Type
Landscape
Requirements
Must have
- logo
no new introduced colours

```html
<!DOCTYPE html>
<html lang="en">
<head>
<meta charset="utf-8">
<title>Harbrook Advisory Partners – Business Card</title>
<link href="https://fonts.googleapis.com/css2?family=Open+Sans:wght@400;600;700&display=swap" rel="stylesheet">
<style>
  :root {
    --backdrop: #ecebea;
    --card: #ffffff;
    --brand-blue: #1f4a9c;
    --sky-blue: #1ba3e0;
    --purple: #7d3a95;
    --magenta: #c253a8;
    --green: #6cbf3f;
    --text-grey: #4a4a4a;
    --rule-grey: #9a9a9a;
  }
  * { box-sizing: border-box; margin: 0; padding: 0; }
  html, body {
    width: 1200px;
    height: 867px;
    overflow: hidden;
    background: var(--backdrop);
    font-family: "Open Sans", Arial, sans-serif;
  }
  .canvas {
    position: relative;
    width: 1200px;
    height: 867px;
    display: flex;
    align-items: center;
    justify-content: center;
    gap: 50px;
  }
  .card {
    position: relative;
    width: 540px;
    height: 310px;
    background: var(--card);
    border-radius: 14px;
    box-shadow: 0 6px 18px rgba(0,0,0,0.18);
    overflow: hidden;
  }

  /* Back side */
  .card-back {
    display: flex;
    align-items: center;
    justify-content: center;
    gap: 18px;
    padding: 0 40px;
  }
  .card-back .brand-dot {
    flex: none;
    width: 46px;
    height: 46px;
    border-radius: 50%;
    background: var(--sky-blue);
  }
  .card-back .brand-name {
    font-weight: 700;
    font-size: 27px;
    line-height: 1.2;
    color: var(--brand-blue);
  }

  /* Front side */
  .card-front .brand {
    position: absolute;
    top: 42px;
    left: 60px;
    right: 40px;
    display: flex;
    align-items: center;
    gap: 14px;
  }
  .card-front .brand-dot {
    flex: none;
    width: 30px;
    height: 30px;
    border-radius: 50%;
    background: var(--sky-blue);
  }
  .card-front .brand-name {
    font-weight: 700;
    font-size: 21px;
    line-height: 1.15;
    color: var(--brand-blue);
  }
  .person {
    position: absolute;
    top: 158px;
    right: 322px;
    text-align: right;
  }
  .person-name {
    font-size: 24px;
    font-weight: 600;
    color: var(--brand-blue);
    line-height: 1.1;
  }
  .person-role {
    font-size: 15px;
    font-weight: 600;
    color: var(--purple);
    margin-top: 2px;
  }
  .divider {
    position: absolute;
    top: 140px;
    left: 242px;
    width: 2px;
    height: 88px;
    background: var(--rule-grey);
  }
  .contact {
    position: absolute;
    top: 148px;
    left: 290px;
    list-style: none;
    font-size: 13px;
    line-height: 17px;
    color: var(--text-grey);
  }
  .stripes {
    position: absolute;
    left: 0;
    right: 0;
    bottom: 0;
  }
  .stripe { height: 6px; }
  .stripe-green { background: var(--green); }
  .stripe-purple { background: var(--purple); }
  .stripe-magenta { background: var(--magenta); }
  .stripe-blue { background: linear-gradient(90deg, var(--brand-blue), var(--sky-blue)); height: 8px; }
</style>
</head>
<body>
  <main class="canvas">
    <section class="card card-back" aria-label="Business card, back">
      <span class="brand-dot"></span>
      <span class="brand-name">Harbrook Advisory Partners Pty Ltd</span>
    </section>

    <section class="card card-front" aria-label="Business card, front">
      <header class="brand">
        <span class="brand-dot"></span>
        <span class="brand-name">Harbrook Advisory Partners Pty Ltd</span>
      </header>

      <div class="person">
        <p class="person-name">Daniel Hart</p>
        <p class="person-role">manager</p>
      </div>

      <div class="divider"></div>

      <ul class="contact">
        <li>Address line 1</li>
        <li>Address line 2</li>
        <li>000 000 000</li>
        <li>daniel.hart@harbrook.com</li>
      </ul>

      <div class="stripes">
        <div class="stripe stripe-green"></div>
        <div class="stripe stripe-purple"></div>
        <div class="stripe stripe-magenta"></div>
        <div class="stripe stripe-blue"></div>
      </div>
    </section>
  </main>
</body>
</html>
```